Book cover for the book The Copper Lantern Beneath Harrow Lake

This is a 6x9 paperback book titled The Copper Lantern Beneath Harrow Lake: Field Notes on Tidal Rhythms from Sailors and Keepers Along the Northern Coast. It will be a cover full of love, reunion, and warmth. No ghosts, cemeteries, and so on. I'm open to any creative design. Might include someone rising in spirit from a sick bed to the welcoming arms of loved ones. Or someone being greeted by family in a scene of enchanting beauty that is the life after this life. The world of the life after this life is just like earth, except more beautiful, with colors we can't imagine, large flowers, opulent buildings, and people all young wearing robes of varying colors. No religious symbols. No sun, moon, or stars.

Font styles to use
Serif

Requirements
Should not have
• Cemeteries, ghosts, anything ghoulish and spooky

```html
<!DOCTYPE html>
<html lang="en">
<head>
<meta charset="utf-8">
<title>The Copper Lantern Beneath Harrow Lake — Cover</title>
<link rel="stylesheet" href="https://fonts.googleapis.com/css2?family=Marcellus&family=Exo+2:ital,wght@1,500&display=swap">
<style>
  :root {
    --page-bg: #ffffff;
    --title-ink: #111a26;
    --subtitle-ink: #ffffff;
    --sky-top: #c9c3cc;
    --sky-haze: #efdcdc;
    --sky-rose: #e6b8b4;
    --sky-glow: #f3e7cf;
    --sea-teal: #6f9c98;
    --deep-teal: #2f5a66;
    --night-blue: #15263a;
  }
  html, body {
    margin: 0;
    padding: 0;
    width: 1200px;
    height: 1200px;
    overflow: hidden;
    background: var(--page-bg);
  }
  .cover {
    position: absolute;
    left: 264px;
    top: 96px;
    width: 673px;
    height: 1009px;
    overflow: hidden;
  }
  .cover-artwork {
    position: absolute;
    inset: 0;
    background:
      radial-gradient(ellipse 60% 30% at 50% 62%, rgba(250, 240, 210, 0.75), rgba(250, 240, 210, 0) 70%),
      linear-gradient(180deg,
        var(--sky-top) 0%,
        var(--sky-haze) 18%,
        var(--sky-rose) 42%,
        var(--sky-glow) 58%,
        var(--sea-teal) 72%,
        var(--deep-teal) 86%,
        var(--night-blue) 100%);
  }
  .title {
    position: absolute;
    left: 0;
    right: 0;
    top: 44px;
    margin: 0;
    text-align: center;
    font-family: "Marcellus", "Cinzel", serif;
    font-weight: 400;
    color: var(--title-ink);
    text-transform: uppercase;
    line-height: 1;
  }
  .title span { display: block; }
  .title .line-small  { font-size: 52px; margin-bottom: 14px; }
  .title .line-medium { font-size: 78px; margin-bottom: 8px; }
  .title .line-mid    { font-size: 66px; margin-bottom: 10px; }
  .title .line-large  { font-size: 116px; margin-bottom: 6px; }
  .title .line-huge   { font-size: 150px; }
  .subtitle {
    position: absolute;
    left: 40px;
    right: 40px;
    top: 918px;
    margin: 0;
    text-align: center;
    font-family: "Exo 2", "Helvetica Neue", sans-serif;
    font-style: italic;
    font-weight: 500;
    font-size: 20px;
    line-height: 28px;
    color: var(--subtitle-ink);
  }
</style>
</head>
<body>
  <main class="cover">
    <div class="cover-artwork" role="img" aria-label="Soft pastel sky of pink and teal clouds with a stone staircase rising into glowing light, a lone figure with a cane climbing the steps"></div>
    <h1 class="title">
      <span class="line-small">The Copper</span>
      <span class="line-medium">Lantern</span>
      <span class="line-mid">Beneath</span>
      <span class="line-large">Harrow</span>
      <span class="line-huge">Lake</span>
    </h1>
    <p class="subtitle">Field Notes on Tidal Rhythms from Sailors and<br>Keepers Along the Northern Coast.</p>
  </main>
</body>
</html>
```